'Cradle Ahead' promotional brochure

We have designed a 6 week program to educate impending first-time parents about the things they need to know to survive the first 6 months. Sessions delivered by general practitioner/family doctor, dietician, physiotherapist, speech pathologist and psychologist. Our promotional blurb is: 'A comprehensive education program for first-time parents-to-be, delivered over 6 weeks by health professionals in your community, about everything you need to know to look after your baby (and yourself!) in the first 6 months'. I now want to put together a promotional brochure to be distributed to those couples who express an interest which will provide further details of what will be delivered in the course.
Updates
In terms of layout, I envisaged a double sided A4 size, foldable into 3 sections, but very happy to be guided on this.
Target Market(s)
To appeal to a young, well educated demographic. First time parents couples.
Industry/Entity Type
Medical
Font styles to use
Other font styles liked:
- Playfair Display
Requirements
Must have
- Playfair display font to be consistent with our logo (attached). Logo also included please. Some consistency with colours of logo please.
Nice to have
- I am a doctor, and have no creative genes! But prefer a clean and professional appearance overall. Not too cluttered in overall appearance.
Should not have
- No cheesy pictures of babies.

```html
<!DOCTYPE html>
<html lang="en">
<head>
<meta charset="utf-8">
<title>Cradle Ahead – Trifold Brochure</title>
<link rel="stylesheet" href="https://fonts.googleapis.com/css2?family=Playfair+Display:wght@400;700&display=swap">
<style>
  :root {
    --brand-green: #6cc04a;
    --paper: #fdfdfe;
    --ink: #111111;
    --muted-grey: #9a9a9a;
    --logo-bg: #f3f4f3;
    --backdrop: #000000;
    --photo-light: #dfe3e6;
    --photo-warm: #caa58c;
  }
  * { margin: 0; padding: 0; box-sizing: border-box; }
  html, body {
    width: 1200px; height: 1000px; overflow: hidden;
    background: var(--backdrop);
    font-family: "Playfair Display", Georgia, serif;
  }
  .canvas { position: relative; width: 1200px; height: 1000px; background: var(--backdrop); }
  .sheet {
    position: absolute; left: 5px; top: 82px; width: 1190px; height: 836px;
    background: var(--paper);
  }
  .abs { position: absolute; }
  .centered { text-align: center; }

  /* Left panel */
  .panel-info {
    left: 19px; top: 19px; width: 356px; height: 798px;
    background: var(--brand-green); color: #fff;
  }
  .info-lead { left: 0; width: 100%; top: 153px; font-size: 17.5px; font-weight: 700; line-height: 24px; }
  .info-body { left: 0; width: 100%; top: 372px; font-size: 17.5px; font-weight: 400; line-height: 24px; }
  .info-body strong { font-weight: 700; }
  .rule-white { left: 104px; width: 146px; height: 4px; background: #fff; }
  .cost-label { left: 0; width: 100%; top: 614px; font-size: 31px; font-weight: 700; line-height: 40px; }
  .cost-value { left: 0; width: 100%; top: 662px; font-size: 35px; font-weight: 700; line-height: 44px; }

  /* Middle panel */
  .contact-heading { left: 420px; width: 344px; top: 152px; font-size: 18px; font-weight: 700; line-height: 24px; color: var(--ink); }
  .contact-phone { left: 420px; width: 344px; top: 203px; font-size: 32px; font-weight: 400; color: var(--ink); }
  .rule-green { height: 4px; background: var(--brand-green); }

  /* Wordmark */
  .wordmark {
    background: var(--logo-bg);
    display: flex; align-items: center; gap: 18px; padding-left: 20px;
  }
  .wordmark-square { width: 34px; height: 34px; background: var(--brand-green); flex: none; }
  .wordmark-name {
    color: var(--brand-green); font-weight: 400;
    font-size: 27px; line-height: 30px; letter-spacing: 0.5px;
  }

  /* Right panel */
  .panel-cover {
    left: 811px; top: 19px; width: 354px; height: 798px;
    border: 3px solid var(--brand-green);
  }
  .cover-divider { left: 0; top: 514px; width: 100%; height: 3px; background: var(--brand-green); }
  .cover-title { left: 0; width: 100%; top: 358px; font-size: 37px; font-weight: 700; color: var(--brand-green); line-height: 44px; }
  .cover-tagline { left: 10px; width: 328px; top: 410px; font-size: 17px; font-weight: 700; color: var(--muted-grey); line-height: 24px; }
  .cover-photo {
    left: 1px; top: 517px; width: 346px; height: 275px;
    background: linear-gradient(135deg, var(--photo-light) 0%, #e9e4df 45%, var(--photo-warm) 100%);
  }
</style>
</head>
<body>
<div class="canvas">
  <div class="sheet">

    <section class="abs panel-info">
      <p class="abs centered info-lead">DELIVERED OVER 6 WEEKS<br>BY HEALTH PROFESSIONALS<br>IN YOUR COMUNITY</p>
      <div class="abs rule-white" style="top:271px"></div>
      <p class="abs centered info-body">EVERYTHING YOU NEED TO<br>KNOW TO LOOK AFTER YOUR<br>BABY (AND YOURSELF)<br><strong>IN THE FIRST 6 MONTHS</strong></p>
      <div class="abs rule-white" style="top:520px"></div>
      <p class="abs centered cost-label">TOTAL COST</p>
      <p class="abs centered cost-value">$300</p>
    </section>

    <section class="panel-contact">
      <p class="abs centered contact-heading">CONTACT DETAILS FOR<br>ENQUIRIES/BOOKINGS</p>
      <p class="abs centered contact-phone">(02) 5550 1234</p>
      <div class="abs rule-green" style="left:520px; top:416px; width:145px"></div>
      <div class="abs wordmark" style="left:432px; top:606px; width:327px; height:124px">
        <span class="wordmark-square"></span>
        <span class="wordmark-name">WATTLEBROOK<br>HEALTH &amp;<br>MEDICAL</span>
      </div>
    </section>

    <section class="abs panel-cover">
      <div class="abs wordmark" style="left:13px; top:98px; width:328px; height:126px">
        <span class="wordmark-square"></span>
        <span class="wordmark-name">WATTLEBROOK<br>HEALTH &amp;<br>MEDICAL</span>
      </div>
      <div class="abs rule-green" style="left:101px; top:274px; width:146px"></div>
      <h1 class="abs centered cover-title">CRADLE AHEAD</h1>
      <p class="abs centered cover-tagline">A COMPREHENSIVE EDUCATION<br>PROGRAM FOR FIRST-TIME<br>PARENTS</p>
      <div class="abs cover-divider"></div>
      <div class="abs cover-photo" role="img" aria-label="Photo of smiling young parents holding their baby"></div>
    </section>

  </div>
</div>
</body>
</html>
```